Banner & also another minor digital image for an Online Academic Journal

A direct example of what I need can be found in this webpage: http://papers.tbhu-archive.org/qrvt/
(Please see attached files, "sAMPLE", and "sAMPLE 2", so you can see what I mean.)
This link (http://papers.tbhu-archive.org/qrvt/) is for an existing ONLINE ACADEMIC JOURNAL at the Thornbury Hill University.
It will help for you to be acquainted with the format of Online Academic Journals.
You will find that there is a banner on top as well as a digital image of a journal/book cover on the right.
I need a
(1) banner and
a (2) digital journal/book cover
for a website for an ONLINE ACADEMIC JOURNAL.
I am looking for a serious, professional, elegant design.
There will not be a print version. Only web-based online publication. No coding needed, only PSD, JPG/PNG and PDF.
1) We use PelloWave (http://archives.pellowave.com/repository-software/journals/) for the digital image of the journal/book cover layout. Link shows the general layout of the journal website.
2) For the digital image of the journal/book cover and also the banner,
Name of the journal is....
"Lumen: A Quarterly of Civic Ethics and Recovery Work"
Only this text will be used and applied to both banner and cover.
***The color associated with the theme of dignity is purple
****You could also add the color red.
*****I don't want the design to be garish, but accents in red might represent
the sexual exploitation and violence in the title.
3) Attached "sAmple 2" file is a basic design for the digital image of the journal/book cover from PelloWave. I am looking for something more elegant and professional looking. Your creativity is encouraged. I am open to receiving your interpretation.
Target Market(s)
Academics & Community Professionals
Industry/Entity Type
Non Profit
Contact Information for Business Card
Match journal design

```html
<!DOCTYPE html>
<html lang="en">
<head>
<meta charset="utf-8">
<title>Lumen – Banner and Cover</title>
<link rel="stylesheet" href="https://fonts.googleapis.com/css2?family=Roboto:wght@300&display=swap">
<style>
  :root {
    --paper: #ffffff;
    --ink-light: #ffffff;
    --deep-violet: #2d1f5c;
    --violet: #4f3f8c;
    --wine: #7e1c3a;
    --crimson: #d81e22;
    --scarlet: #ee1c1c;
  }
  * { margin: 0; padding: 0; box-sizing: border-box; }
  html, body {
    width: 1200px;
    height: 746px;
    overflow: hidden;
    background: var(--paper);
  }
  .canvas {
    position: relative;
    width: 1200px;
    height: 746px;
  }

  /* Banner */
  .banner {
    position: absolute;
    left: 119px;
    top: 127px;
    width: 980px;
    height: 125px;
  }
  .banner__strip {
    position: absolute;
    left: 0; top: 0;
    width: 100%;
    height: 20px;
    background: linear-gradient(90deg, var(--deep-violet) 0%, var(--deep-violet) 42%, var(--wine) 68%, var(--scarlet) 100%);
  }
  .banner__band {
    position: absolute;
    left: 0; top: 20px;
    width: 100%;
    height: 105px;
    background:
      linear-gradient(180deg, rgba(255,255,255,0.06) 0%, rgba(255,255,255,0) 40%, rgba(0,0,0,0.05) 100%),
      linear-gradient(90deg, var(--violet) 0%, #54408a 35%, #7a3a6e 55%, #c9303a 78%, var(--crimson) 100%);
  }
  .banner__title {
    position: absolute;
    left: 41px; top: 50px;
    font-family: "Roboto", sans-serif;
    font-weight: 300;
    font-size: 40px;
    line-height: 1;
    color: var(--ink-light);
  }
  .banner__subtitle {
    position: absolute;
    right: 37px; top: 59px;
    font-family: "Roboto", sans-serif;
    font-weight: 300;
    font-size: 26px;
    line-height: 1;
    color: var(--ink-light);
    white-space: nowrap;
  }

  /* Cover */
  .cover {
    position: absolute;
    left: 851px;
    top: 305px;
    width: 247px;
    height: 317px;
    overflow: hidden;
    background: linear-gradient(180deg, #4a3080 0%, #553076 28%, #7c2546 55%, #b8212c 80%, var(--crimson) 100%);
  }
  .cover__spine {
    position: absolute;
    left: 0; top: 0;
    width: 33px; height: 100%;
    background: linear-gradient(180deg, rgba(20,10,50,0.45) 0%, rgba(40,10,30,0.35) 60%, rgba(90,0,0,0.3) 100%);
  }
  .cover__band {
    position: absolute;
    left: 0; top: 103px;
    width: 100%; height: 86px;
    background: linear-gradient(180deg, rgba(255,255,255,0.14) 0%, rgba(255,255,255,0.06) 30%, rgba(255,255,255,0.03) 75%, rgba(255,255,255,0.12) 100%);
  }
  .cover__title {
    position: absolute;
    left: 44px; top: 134px;
    font-family: "Roboto", sans-serif;
    font-weight: 300;
    font-size: 32px;
    line-height: 1;
    color: var(--ink-light);
  }
  .cover__subtitle {
    position: absolute;
    right: 41px; top: 199px;
    font-family: "Roboto", sans-serif;
    font-weight: 300;
    font-size: 18px;
    line-height: 20.5px;
    text-align: right;
    color: var(--ink-light);
  }
</style>
</head>
<body>
<main class="canvas">

  <header class="banner">
    <div class="banner__strip"></div>
    <div class="banner__band"></div>
    <h1 class="banner__title">Lumen</h1>
    <p class="banner__subtitle">A Quarterly of Civic Ethics and Recovery Work</p>
  </header>

  <section class="cover" aria-label="Journal cover">
    <div class="cover__spine"></div>
    <div class="cover__band"></div>
    <h2 class="cover__title">Lumen</h2>
    <p class="cover__subtitle">A Quarterly<br>of Civic Ethics<br>and Recovery<br>Work</p>
  </section>

</main>
</body>
</html>
```